Water Filter Company Needs Bizz Cards!!

Need business cards for my company. We sell whole home water filters and salt free water softeners. No more buying bottled water. Our filtering units filter out all heavy metals, chlorine, and VOC's, last 15 years, and are maintenance free and supply your whole home with spring quality alkaline water. Our Salt free water conditioners, eliminate hard water and scale, without lowering the ph, or TDS's (total Dissolved solids)

I think this is the color code we are using on my site. My logo looks good behind it. #192841

Website will be www.Brovexa.com

Industry/Entity Type

Water Purification

Contact Information for Business Card

For now, just insert standard Dummy text. I need these text lines for the info to be editable so i can make them for multiple employees. I do have Photoshop and illustrator, unless there is a simpler program i can use solely for biz cards

Font styles to use
Sans Serif

Requirements
Must have
• Use my preexisting logo.

www.BroVexa.com

Spring Quality Alkaline Water at every tap.

List out services. Whole Home Water Filters, Salt Free Water Softeners, Clarimont KT7, UV Sterilizers
Nice to have
• I think this is the color code we are using on my site. My logo looks good behind it. #192841 or black. Please no white or light blue backgrounds.

Maybe a picture of my tank.

Slogan like Spring Quality Alkaline Water at every tap.
And just list the services Whole Home Water Filters, Salt Free Water Softeners, Clarimont KT7, UV Sterilizers

I think I would like to not have a contrasting textured logo like I see on some of them. I may use it for my personal cards, but new employees may not want the extra expense.
Should not have
• A different logo than the one provided.

White or baby blue backgrounds. Use the color code, or blacks.

```html
<!DOCTYPE html>
<html lang="en">
<head>
<meta charset="utf-8">
<title>Brovexa Business Card</title>
<link rel="stylesheet" href="https://fonts.googleapis.com/css2?family=Work+Sans:wght@400;500;600&display=swap">
<style>
  :root {
    --page: #d9d3cb;
    --card-top: #232325;
    --card-bottom: #141416;
    --accent: #1e9ad6;
    --accent-light: #8fd0ee;
    --text: #d8d2cb;
    --text-muted: #b9b2aa;
  }
  * { box-sizing: border-box; margin: 0; padding: 0; }
  html, body {
    width: 1200px; height: 887px; overflow: hidden;
    background: var(--page);
    font-family: "Work Sans", Arial, sans-serif;
  }
  .canvas { position: relative; width: 1200px; height: 887px; }
  .card {
    position: absolute; left: 80px; top: 158px;
    width: 1040px; height: 571px;
    border-radius: 26px;
    background: linear-gradient(160deg, var(--card-top), var(--card-bottom));
    box-shadow: 0 14px 40px rgba(0,0,0,.25);
    overflow: hidden;
  }
  .brand {
    position: absolute; left: 58px; top: 58px;
    display: flex; align-items: center; gap: 14px;
  }
  .brand-dot {
    width: 44px; height: 44px; border-radius: 50%;
    background: var(--accent);
  }
  .brand-name {
    font-size: 58px; font-weight: 600; line-height: 1;
    color: var(--accent); letter-spacing: -1px;
  }
  .slogan {
    position: absolute; left: 58px; top: 128px;
    font-size: 17px; font-weight: 500; letter-spacing: .5px;
    color: var(--accent-light);
  }
  .services {
    position: absolute; left: 58px; top: 158px;
    display: flex; flex-wrap: wrap; gap: 4px 18px;
    width: 520px; list-style: none;
    font-size: 15px; color: var(--text-muted); letter-spacing: .3px;
  }
  .service-item { display: flex; align-items: center; gap: 7px; }
  .service-item::before {
    content: ""; width: 5px; height: 5px; border-radius: 50%;
    background: var(--accent);
  }
  .accent-bar {
    position: absolute; left: 0; top: 235px;
    width: 16px; height: 60px; background: var(--accent);
  }
  .person-name {
    position: absolute; left: 58px; top: 228px;
    font-size: 32px; font-weight: 500; letter-spacing: 2px;
    color: var(--accent);
  }
  .person-role {
    position: absolute; left: 58px; top: 272px;
    font-size: 24px; font-weight: 400; color: var(--text);
  }
  .divider {
    position: absolute; left: 58px; top: 323px;
    width: 18px; height: 2px; background: var(--text-muted);
  }
  .address {
    position: absolute; left: 58px; top: 342px;
    font-size: 24px; line-height: 34px; color: var(--text);
    letter-spacing: .5px; font-style: normal;
  }
  .contact-list {
    position: absolute; left: 58px; top: 420px;
    list-style: none;
  }
  .contact-item {
    display: flex; align-items: center; gap: 12px;
    height: 35px; font-size: 24px; letter-spacing: .5px;
    color: var(--text);
  }
  .contact-icon { width: 16px; height: 16px; flex: none; }
  .brand-decoration {
    position: absolute; left: 641px; top: 50px;
    width: 350px; height: 480px; border-radius: 50%;
    background: radial-gradient(ellipse at 50% 60%, rgba(143,208,238,.75) 0%, rgba(30,154,214,.6) 50%, rgba(30,154,214,0) 72%);
  }
</style>
</head>
<body>
<div class="canvas">
  <section class="card">
    <div class="brand">
      <span class="brand-dot"></span>
      <span class="brand-name">Brovexa</span>
    </div>
    <p class="slogan">Spring Quality Alkaline Water at every tap.</p>
    <ul class="services">
      <li class="service-item">Whole Home Water Filters</li>
      <li class="service-item">Salt Free Water Softeners</li>
      <li class="service-item">Clarimont KT7</li>
      <li class="service-item">UV Sterilizers</li>
    </ul>

    <div class="accent-bar"></div>
    <h1 class="person-name">DANIEL CARTER</h1>
    <p class="person-role">Founder</p>
    <div class="divider"></div>
    <address class="address">42 Linden Park Rd,<br>Westbrook, Oregon</address>

    <ul class="contact-list">
      <li class="contact-item">
        <svg class="contact-icon" viewBox="0 0 16 16"><path d="M3 1l3 3-2 2c1 2 3 4 5 5l2-2 3 3-2 3C7 15 1 9 1 3z" fill="var(--accent)"/></svg>
        84 0912 555 017
      </li>
      <li class="contact-item">
        <svg class="contact-icon" viewBox="0 0 16 16"><rect x="1.5" y="3.5" width="13" height="9" fill="none" stroke="var(--accent)" stroke-width="1.5"/><path d="M1.5 3.5l6.5 5 6.5-5" fill="none" stroke="var(--accent)" stroke-width="1.5"/></svg>
        info@Brovexa.com
      </li>
      <li class="contact-item">
        <svg class="contact-icon" viewBox="0 0 16 16"><circle cx="8" cy="8" r="6.5" fill="none" stroke="var(--accent)" stroke-width="1.3"/><ellipse cx="8" cy="8" rx="3" ry="6.5" fill="none" stroke="var(--accent)" stroke-width="1.2"/><path d="M1.5 8h13" stroke="var(--accent)" stroke-width="1.2"/></svg>
        www.Brovexa.com
      </li>
    </ul>

    <div class="brand-decoration" role="img" aria-label="Large brand symbol decoration area"></div>
  </section>
</div>
</body>
</html>
```